Belzo business card

I'm a hack at Illustrator, but have put together a set of business cards as attached. If someone could please improve these including good font selection, standard font sizes and spacing, nice layout and symmetry. Rear side the same on all cards. Basically make these cards into something impressive and professional.
Updates

Official logo just uploaded, please use these colours

Target Market(s)

50+ year old married couples

Industry/Entity Type

Business

Requirements
Must have
• Professional
Should not have
• Silly, cartoony

```html
<!DOCTYPE html>
<html lang="en">
<head>
<meta charset="utf-8">
<title>Belzo Business Card</title>
<link rel="stylesheet" href="https://fonts.googleapis.com/css2?family=Arimo:wght@400;700&family=Jost:wght@600&display=swap">
<style>
  :root {
    --paper: #ffffff;
    --ink: #111111;
    --brand-teal: #219a8c;
    --brand-dark: #1d3a3a;
    --frame: #222222;
  }
  * { margin: 0; padding: 0; box-sizing: border-box; }
  html, body {
    width: 1200px;
    height: 900px;
    overflow: hidden;
    background: var(--paper);
  }
  .canvas {
    position: relative;
    width: 1200px;
    height: 900px;
    background: var(--paper);
    font-family: "Arimo", Arial, sans-serif;
    color: var(--ink);
  }
  .card {
    position: absolute;
    left: 68px;
    top: 125px;
    width: 1064px;
    height: 650px;
    border: 2px solid var(--frame);
  }
  .contact {
    position: absolute;
    left: 36px;
    top: 28px;
    font-size: 40px;
    line-height: 47px;
  }
  .brand {
    position: absolute;
    right: 86px;
    top: 100px;
    display: flex;
    align-items: center;
    gap: 18px;
  }
  .brand-square {
    width: 38px;
    height: 38px;
    background: var(--brand-teal);
  }
  .brand-name {
    font-family: "Arimo", Arial, sans-serif;
    font-weight: 700;
    font-size: 64px;
    letter-spacing: 10px;
    color: var(--brand-teal);
  }
  .person {
    position: absolute;
    right: 38px;
    top: 286px;
    text-align: right;
  }
  .person-name {
    font-size: 46px;
    font-weight: 700;
    line-height: 56px;
    margin-bottom: 2px;
  }
  .person-role {
    font-size: 26px;
    line-height: 34.5px;
  }
  .divider {
    position: absolute;
    left: 17px;
    right: 17px;
    top: 526px;
    height: 4px;
    background: var(--brand-dark);
  }
  .company-details {
    position: absolute;
    left: 0;
    right: 0;
    top: 546px;
    text-align: center;
    font-family: "Jost", "Century Gothic", sans-serif;
    font-weight: 600;
    font-size: 28px;
    line-height: 50px;
    color: var(--brand-dark);
  }
</style>
</head>
<body>
<main class="canvas">
  <section class="card">
    <div class="contact">
      <p>M: 0400 555 217</p>
      <p>D: 03 9555 2048</p>
      <p>leyla.ardan@belzo.com.au</p>
    </div>

    <div class="brand">
      <span class="brand-square"></span>
      <span class="brand-name">BELZO</span>
    </div>

    <div class="person">
      <h1 class="person-name">Leyla Ardan</h1>
      <p class="person-role">Sustainable Building Designer</p>
      <p class="person-role">B.Sc. Architecture</p>
      <p class="person-role">M.Sc. Renewable Energy</p>
      <p class="person-role">and Architecture</p>
    </div>

    <div class="divider"></div>

    <div class="company-details">
      <p>8/41 Hart St Kelvale, VIC 3150, Australia Ph.: (+61) 0395550190</p>
      <p>www.belzo.com.au | REC 30418 ABN XXXXXXXXXXX</p>
    </div>
  </section>
</main>
</body>
</html>
```